Heronwick Lodge Sign

Heronwick Lodge is a lake resort in Branson, MO
This resort used to have 66 units however the resort was sold in sections. I own the part of the resort that has all the amenities listed on the attached file. We need an updated sign and also billboard.
On a sign like this should be include a phone number?

```html
<!DOCTYPE html>
<html lang="en">
<head>
<meta charset="utf-8">
<title>Heronwick Lodge Sign</title>
<link rel="stylesheet" href="https://fonts.googleapis.com/css2?family=Jost:wght@300;400;700&display=swap">
<style>
  :root {
    --lake-blue: #0524c4;
    --leaf-green: #6ced12;
    --sun-yellow: #eef524;
    --paper: #ffffff;
  }
  * { margin: 0; padding: 0; box-sizing: border-box; }
  html, body { width: 1200px; height: 900px; overflow: hidden; background: var(--paper); }
  .sign {
    position: relative;
    width: 1200px;
    height: 900px;
    background: var(--paper);
    font-family: "Jost", "Futura", sans-serif;
    color: var(--lake-blue);
  }
  .brand {
    position: absolute;
    top: 92px;
    left: 0;
    width: 1200px;
    text-align: center;
  }
  .brand-name {
    font-weight: 700;
    font-size: 96px;
    line-height: 1;
    letter-spacing: -2px;
    color: var(--lake-blue);
  }
  .brand-place {
    margin-top: 22px;
    font-weight: 300;
    font-size: 54px;
    line-height: 1;
    letter-spacing: -0.5px;
    color: var(--lake-blue);
  }
  .amenities {
    position: absolute;
    top: 362px;
    list-style: none;
    font-weight: 700;
    font-size: 28px;
    line-height: 37.5px;
  }
  .amenities li { position: relative; padding-left: 18px; white-space: nowrap; }
  .amenities li::before {
    content: "";
    position: absolute;
    left: 0;
    top: 15px;
    width: 9px;
    height: 9px;
    border-radius: 50%;
    background: var(--leaf-green);
  }
  .amenities-left { left: 65px; }
  .amenities-right { left: 655px; }
  .amenities-right li { padding-left: 22px; }
  .column-divider {
    position: absolute;
    left: 555px;
    top: 368px;
    width: 4px;
    height: 289px;
    background: var(--leaf-green);
  }
  .shoreline {
    position: absolute;
    left: 0;
    top: 0;
    width: 1200px;
    height: 900px;
  }
  .fish-art {
    position: absolute;
    left: 474px;
    top: 746px;
    width: 140px;
    height: 38px;
    border-radius: 19px;
    background: linear-gradient(90deg, rgba(255,255,255,0.15), rgba(255,255,255,0.45));
  }
  .contact {
    position: absolute;
    left: 42px;
    right: 40px;
    top: 790px;
    display: flex;
    justify-content: space-between;
    align-items: baseline;
    font-weight: 700;
  }
  .contact-address, .contact-web { font-size: 32px; color: var(--paper); }
  .contact-phone {
    font-size: 74px;
    line-height: 1;
    letter-spacing: -1px;
    color: var(--sun-yellow);
  }
</style>
</head>
<body>
<main class="sign">
  <header class="brand">
    <h1 class="brand-name">Heronwick Lodge</h1>
    <p class="brand-place">on Table Rock Lake</p>
  </header>

  <ul class="amenities amenities-left">
    <li>Direct Lake access</li>
    <li>Swim Decks</li>
    <li>Slip Rentals</li>
    <li>Boat Rentals</li>
    <li>Indoor Pool</li>
    <li>Golf Carts</li>
    <li>Pantoon Boats</li>
    <li>Kayak - Paddleboards</li>
  </ul>
  <div class="column-divider"></div>
  <ul class="amenities amenities-right">
    <li>1-3 Bedroom Vacation Rentals</li>
    <li>Dining Hall</li>
    <li>Game Room</li>
    <li>Children’s Activities</li>
    <li>Pet Friendly</li>
    <li>Gift Store</li>
    <li>Outdoor Games</li>
    <li>Family Reunions - Large Groups</li>
  </ul>

  <svg class="shoreline" viewBox="0 0 1200 900" aria-hidden="true">
    <path d="M0 724 Q150 704 300 726 T600 712 T900 730 T1200 716 V900 H0 Z" fill="var(--lake-blue)"/>
    <path d="M0 694 Q150 676 300 698 T600 684 T900 702 T1200 688" fill="none" stroke="var(--leaf-green)" stroke-width="7"/>
  </svg>

  <div class="fish-art" role="img" aria-label="Small white line drawing of a fish skeleton"></div>

  <footer class="contact">
    <span class="contact-address">22 Heron Lane</span>
    <span class="contact-phone">800-555-0143</span>
    <span class="contact-web">Heronwicklodge.com</span>
  </footer>
</main>
</body>
</html>
```